TOLV.
RAKESH ENTERTAINMENT & MEDIA
Use specific fonts
any thing which suits with the LOGO provided
Professional
RAKESH MEHTA
MR.
D-47, NORTH PARK-II , GURGAON 122001,HARYANA, INDIA
rakesh@tolv.co.in
www.tolv.co.in
LOG IN THE CENTRE

```html
<!DOCTYPE html>
<html lang="en">
<head>
<meta charset="utf-8">
<title>TOLV Stationery Set</title>
<link href="https://fonts.googleapis.com/css2?family=Open+Sans:wght@400;800&display=swap" rel="stylesheet">
<style>
:root{
  --bg:#3a3a3c;
  --paper:#ffffff;
  --brand:#1d4f86;
  --teal:#1f8fb4;
  --teal-deep:#0f6c8f;
  --swoosh:#2b2b2b;
  --ink:#7a7a7a;
  --label:#bdbdbd;
  --ghost:#eef1f4;
}
*{margin:0;padding:0;box-sizing:border-box}
html,body{width:1200px;height:348px;overflow:hidden}
body{background:var(--bg);font-family:"Open Sans",Arial,sans-serif;position:relative}
.piece{position:absolute;background:var(--paper);overflow:hidden;box-shadow:0 2px 6px rgba(0,0,0,.45)}
.wave{position:absolute;left:0;bottom:0;width:100%}
.logo{position:absolute;display:flex;align-items:center;gap:4px;color:var(--brand);font-weight:800;letter-spacing:.5px;line-height:1;white-space:nowrap}
.logo .mark{background:var(--brand);display:inline-block}
.ghost-name{position:absolute;left:0;width:100%;text-align:center;color:var(--ghost);font-weight:800;font-size:54px;line-height:1}
.tiny{position:absolute;color:var(--ink);font-size:3.5px;line-height:5px;white-space:nowrap}
.label{position:absolute;color:var(--label);font-size:5px;white-space:nowrap;transform:translateX(-50%)}

.card-front{left:24px;top:132px;width:132px;height:84px}
.card-back{left:24px;top:240px;width:132px;height:78px}
.letterhead{top:19px;width:223px;height:317px}
.lh-one{left:168px}
.lh-two{left:408px}
.slip{left:643px;width:300px}
.slip-top{top:72px;height:125px}
.slip-bottom{top:211px;height:113px}
.envelope{left:960px;width:216px}
.env-front{top:149px;height:79px}
.env-back{top:240px;height:79px}
</style>
</head>
<body>

<span class="label" style="left:90px;top:122px">Business Cards</span>
<div class="piece card-front">
  <div class="logo" style="left:8px;top:18px;font-size:13px"><span class="mark" style="width:8px;height:8px"></span>TOLV</div>
  <div class="tiny" style="left:80px;top:17px">Contact Name<br>Phone Number<br>Email Address</div>
  <svg class="wave" viewBox="0 0 132 30" height="30" preserveAspectRatio="none">
    <path d="M0 14 C40 22 90 4 132 10 L132 30 L0 30Z" fill="var(--teal)"/>
    <path d="M0 10 C40 18 90 0 132 6 L132 9 C90 3 40 21 0 13Z" fill="var(--swoosh)"/>
  </svg>
</div>
<div class="piece card-back">
  <div class="logo" style="left:44px;top:28px;font-size:11px"><span class="mark" style="width:6px;height:6px"></span>TOLV</div>
  <svg class="wave" viewBox="0 0 132 20" height="20" preserveAspectRatio="none">
    <path d="M0 8 C40 16 90 0 132 6 L132 20 L0 20Z" fill="var(--teal)"/>
    <path d="M0 6 C40 14 90 -2 132 4 L132 6 C90 1 40 16 0 9Z" fill="var(--swoosh)"/>
  </svg>
</div>
<span class="label" style="left:90px;top:322px">Back Side</span>

<div class="piece letterhead lh-one">
  <div class="logo" style="left:30px;top:14px;font-size:13px"><span class="mark" style="width:7px;height:7px"></span>TOLV</div>
  <div class="tiny" style="left:150px;top:14px">Office Address Line<br>Email | Website</div>
  <div class="ghost-name" style="top:130px">TOLV</div>
  <svg class="wave" viewBox="0 0 223 30" height="30" preserveAspectRatio="none">
    <path d="M0 14 C70 26 150 0 223 10 L223 30 L0 30Z" fill="var(--teal)"/>
    <path d="M0 10 C70 22 150 -4 223 6 L223 9 C150 0 70 26 0 14Z" fill="var(--swoosh)"/>
  </svg>
</div>
<span class="label" style="left:280px;top:339px">Letterhead 1</span>

<div class="piece letterhead lh-two">
  <div class="logo" style="left:30px;top:14px;font-size:13px"><span class="mark" style="width:7px;height:7px"></span>TOLV</div>
  <div class="ghost-name" style="top:130px">TOLV</div>
  <svg class="wave" viewBox="0 0 223 30" height="30" preserveAspectRatio="none">
    <path d="M0 14 C70 26 150 0 223 10 L223 30 L0 30Z" fill="var(--teal)"/>
    <path d="M0 10 C70 22 150 -4 223 6 L223 9 C150 0 70 26 0 14Z" fill="var(--swoosh)"/>
  </svg>
</div>
<span class="label" style="left:520px;top:339px">Letterhead 2</span>

<div class="piece slip slip-top">
  <div class="logo" style="left:26px;top:18px;font-size:14px"><span class="mark" style="width:8px;height:8px"></span>TOLV</div>
  <div class="tiny" style="left:26px;top:38px">Company Name<br>Website</div>
  <div class="ghost-name" style="top:30px;left:auto;right:18px;width:auto;font-size:28px">TOLV</div>
  <svg class="wave" viewBox="0 0 300 26" height="26" preserveAspectRatio="none">
    <path d="M0 12 C90 24 200 0 300 9 L300 26 L0 26Z" fill="var(--teal)"/>
    <path d="M0 9 C90 21 200 -3 300 6 L300 9 C200 0 90 24 0 13Z" fill="var(--swoosh)"/>
  </svg>
</div>
<div class="piece slip slip-bottom">
  <div class="logo" style="left:26px;top:18px;font-size:14px"><span class="mark" style="width:8px;height:8px"></span>TOLV</div>
  <svg class="wave" viewBox="0 0 300 26" height="26" preserveAspectRatio="none">
    <path d="M0 12 C90 24 200 0 300 9 L300 26 L0 26Z" fill="var(--teal)"/>
    <path d="M0 9 C90 21 200 -3 300 6 L300 9 C200 0 90 24 0 13Z" fill="var(--swoosh)"/>
  </svg>
</div>
<span class="label" style="left:793px;top:328px">Compliment Slip</span>

<div class="piece envelope env-front">
  <div class="logo" style="left:96px;top:30px;font-size:8px"><span class="mark" style="width:5px;height:5px"></span>TOLV</div>
  <svg class="wave" viewBox="0 0 216 22" height="22" preserveAspectRatio="none">
    <path d="M0 10 C70 20 150 0 216 8 L216 22 L0 22Z" fill="var(--teal)"/>
    <path d="M0 7 C70 17 150 -3 216 5 L216 8 C150 1 70 21 0 10Z" fill="var(--swoosh)"/>
  </svg>
</div>
<div class="piece envelope env-back">
  <svg viewBox="0 0 216 79" width="216" height="79" preserveAspectRatio="none" style="position:absolute;left:0;top:0">
    <path d="M0 0 L108 40 L216 0Z" fill="#f3f5f7" stroke="#d7dbe0" stroke-width="0.6"/>
    <path d="M0 79 L108 44 L216 79" fill="none" stroke="#e1e4e8" stroke-width="0.6"/>
    <path d="M0 0 L216 0 L216 6 C150 2 70 14 0 8Z" fill="var(--teal-deep)"/>
  </svg>
  <div class="logo" style="left:98px;top:52px;font-size:6px"><span class="mark" style="width:4px;height:4px"></span>TOLV</div>
</div>
<span class="label" style="left:1068px;top:323px">Envelope</span>

</body>
</html>
```